BrPeople Business Cards for SME Experts

We need a business card for a new company based in Clearwater FL called Brightfold of People. BrP is your access to on-demand subject matter experts. The final design should be very clean communicating innovation and expertise. Our logo design is attached.

The Information Age has affected the workforce in that automation and computerization have resulted in higher productivity coupled with net job loss of many knowledgeable employees. Combined with the creation of the internet and search capabilities, the disintermediation of the value chain of Subject Matter Experts (SME) has happened. We no longer need to work through traditional consulting firms for all consulting needs, instead the direct access to the SME, through a leaner and lower cost model is what the market is demanding.
BrPeople is a new marketplace to buy consulting services. The business model is that all consultants (subject matter experts) can become a consulting resource in the marketplace following our guidelines. The consumer can now easily access consultants that they could not find easily before.
In much the way an Zaxo car can be identified and requested, so can a BrPeople Consultant. Each consultant can be identified by: location, expertise, billing rate, and prior experience rating.
By seamlessly connecting consultants to requesters through a new Brightfold of People marketplace, you now will have an easy to use and quicker turnaround to request and staff your consulting needs. Leveraging the BrP app, you can access the subject matter expert you need for your business requirement.

Target Market(s)

Small and medium sized companies; non-profits

Industry/Entity Type

Business Consultant

Contact Information for Business Card

Name
website
email address
Logo
mailing address (debating if I really need...)
twitter
LinkedIn

Requirements
Must have
• the logo I have included in the design; want the colors to be consistent with the logo design

```html
<!DOCTYPE html>
<html lang="en">
<head>
<meta charset="utf-8">
<title>Brightfold of People — Business Card</title>
<link href="https://fonts.googleapis.com/css2?family=Outfit:wght@400;500;600;700&display=swap" rel="stylesheet">
<style>
  :root {
    --navy: #2e3486;
    --cyan: #06aecb;
    --card: #f7f7f8;
    --page: #e4e5e9;
    --ink: #2e3486;
  }
  * { margin: 0; padding: 0; box-sizing: border-box; }
  html, body {
    width: 1200px; height: 780px; overflow: hidden;
    background: var(--page);
    font-family: "Outfit", sans-serif;
  }
  .card {
    position: absolute; left: 75px; top: 90px;
    width: 1050px; height: 600px;
    background: var(--card);
    overflow: hidden;
    box-shadow: 0 10px 30px rgba(30, 34, 80, 0.18);
  }
  .band { position: absolute; }
  .band--left-top { left: 160px; top: 0; width: 150px; height: 235px; background: var(--navy); }
  .band--left-bottom { left: 160px; top: 235px; width: 150px; height: 365px; background: var(--cyan); }
  .band--right-top { left: 930px; top: 0; width: 70px; height: 175px; background: var(--cyan); }
  .band--right-bottom { left: 930px; top: 175px; width: 70px; height: 425px; background: var(--navy); }
  .logo-mark {
    position: absolute; left: 232px; top: 160px;
    width: 150px; height: 150px;
  }
  .logo-mark text {
    font-family: "Outfit", sans-serif; font-weight: 700; font-size: 46px; fill: var(--navy);
  }
  .info { position: absolute; left: 400px; top: 190px; color: var(--ink); }
  .company { font-size: 46px; font-weight: 700; letter-spacing: 0.5px; line-height: 1; }
  .company .accent { color: var(--cyan); }
  .person { font-size: 30px; font-weight: 600; margin-top: 28px; }
  .contacts { list-style: none; margin-top: 22px; font-size: 24px; font-weight: 400; line-height: 37px; }
  .contacts .label { color: var(--cyan); font-weight: 600; margin-right: 6px; }
</style>
</head>
<body>
  <main class="card" aria-label="Brightfold of People business card">
    <div class="band band--left-top"></div>
    <div class="band band--left-bottom"></div>
    <div class="band band--right-top"></div>
    <div class="band band--right-bottom"></div>

    <svg class="logo-mark" viewBox="0 0 150 150" aria-label="BrP">
      <circle cx="75" cy="75" r="68" fill="#ffffff" stroke="var(--navy)" stroke-width="6"/>
      <text x="75" y="91" text-anchor="middle">BrP</text>
    </svg>

    <section class="info">
      <h1 class="company">Brightfold of <span class="accent">People</span></h1>
      <p class="person">Employee Name</p>
      <ul class="contacts">
        <li><span class="label">p:</span>000-111-0000</li>
        <li><span class="label">e:</span>abc@yourmail.com</li>
        <li><span class="label">w:</span>www.abcyourwebsite.com</li>
        <li>your address Avenue Harbor Falls, FL 0000</li>
      </ul>
    </section>
  </main>
</body>
</html>
```